Business Card for Realtor in In Town Atlanta

I'd like a business card that look can transfer to my website, stationery, promo pieces, etc.
I work with modern, hip individuals and enjoy a cleaner design. I do NOT sell homes in the suburbs, I work very close to downtown Atlanta and this is a progressive crowd!
I do not want the typical card with my photo on it, I'm interested in more retro modern look. I'm attaching a pdf of my sign so you can see my colors which are a burnt orange, gray and somewhat of a turquoise blue. Again I like simple and mod design. My website will be called thecorelane.com and besides real estate info I will feature local eateries, pubs, music venues, events, etc. that would appeal to the in town city goer. Below are examples of my signs, the Ho/Lux info is required on my card, maybe on the back?
I've also added the HO/LUX balloon logo, you do NOT have to use it, if you do use it I would prefer that it is just a gray scale version of it or white and gray on blue, maybe on the back of the card.

Target Market(s)

The in town real estate market in Atlanta.

Industry/Entity Type

Real Estate Agent

Contact Information for Business Card

Helen Vorst
REALTORĀ®
404.555.0183 cell
www.thecorelane.com
Helen@thecorelane.com and Helen@helenvorst.com
HO/LUXUrban Atlanta Parkview
2274 N. Halvers Brook Avenue
Halvers Park, GA 30390
404.555.0127
404.555.0164 fax

Font styles to use
Sans Serif

Colors
aaaaaa
fdfbfc
f37122
81c7e5

Requirements
Must have
• Clean, modern design.
• Simple, not fussy.
• I need the colors and design to easily transfer to stationery and website.
• REALTORĀ® under my name as my title.
Nice to have
• As far as design elements I like circular shapes to soften the edges, don't want the card to look to hard or serious.
Should not have
• No frills, no photos
• Please DO NOT use black as the base color of the card.

```html
<!DOCTYPE html>
<html lang="en">
<head>
<meta charset="utf-8">
<title>Helen Vorst — Business Card</title>
<link rel="stylesheet" href="https://fonts.googleapis.com/css2?family=Kanit:wght@300;400&family=Aleo:wght@400&display=swap">
<style>
  :root {
    --card-gray: #ababab;
    --band-gray: #7b7b7b;
    --orange: #f37122;
    --orange-soft: #f0915a;
    --orange-deep: #a9582a;
    --orange-glow: #f7962a;
    --white: #fdfbfc;
    --turquoise: #81c7e5;
  }
  * { margin: 0; padding: 0; box-sizing: border-box; }
  html, body { width: 1025px; height: 1200px; overflow: hidden; background: var(--white); }
  body { position: relative; font-family: "Kanit", sans-serif; font-weight: 300; }

  .card-front { position: absolute; left: 0; top: 0; width: 1025px; height: 491px; background: var(--card-gray); }
  .signature-faint {
    position: absolute; left: 170px; top: 0; width: 855px; height: 165px;
    background: linear-gradient(90deg, rgba(240,145,90,0.18), rgba(240,145,90,0.28), rgba(240,145,90,0.12));
    border-radius: 0 0 80px 80px;
  }
  .agent-name {
    position: absolute; left: 174px; top: 246px;
    font-size: 39px; font-weight: 400; color: var(--white); line-height: 1;
  }
  .brokerage-mark {
    position: absolute; left: 214px; top: 424px;
    display: flex; align-items: center; gap: 10px;
    font-size: 26px; font-weight: 400; color: var(--white); line-height: 1;
  }
  .brokerage-mark .dot { width: 16px; height: 16px; border-radius: 50%; background: var(--white); }

  .phones { position: absolute; left: 638px; top: 246px; font-size: 27px; line-height: 35px; color: var(--white); }
  .phones .tag { color: var(--orange); margin-left: 8px; font-size: 25px; }

  .office { position: absolute; left: 638px; top: 380px; font-size: 24px; line-height: 30px; color: var(--white); }
  .office .address { font-weight: 400; }

  .accent-rule { position: absolute; left: 0; top: 491px; width: 1025px; height: 4px; background: var(--orange); }
  .contact-band {
    position: absolute; left: 0; top: 495px; width: 1025px; height: 105px;
    background: var(--band-gray);
    display: flex; align-items: center; justify-content: center; gap: 26px;
    font-size: 25px; color: var(--orange-soft);
  }

  .card-back {
    position: absolute; left: 0; top: 602px; width: 1025px; height: 598px;
    background:
      radial-gradient(ellipse 560px 420px at 50% 88%, var(--orange-glow) 0%, rgba(247,150,42,0) 100%),
      linear-gradient(180deg, var(--orange-deep) 0%, #e0681f 22%, var(--orange) 45%, #f37a22 100%);
  }
  .signature-bright {
    position: absolute; left: 203px; top: 204px; width: 605px; height: 72px;
    background: linear-gradient(90deg, rgba(253,251,252,0.35), rgba(253,251,252,0.5), rgba(253,251,252,0.3));
    border-radius: 36px;
  }
  .tagline {
    position: absolute; left: 0; width: 1025px; top: 282px; text-align: center;
    font-family: "Aleo", serif; font-size: 38px; color: var(--turquoise); line-height: 1;
    padding-left: 16px;
  }
  .back-url {
    position: absolute; left: 0; width: 1025px; top: 520px; text-align: center;
    font-size: 29px; letter-spacing: 2.5px; color: var(--white); line-height: 1;
  }
</style>
</head>
<body>
  <section class="card-front">
    <div class="signature-faint" role="img" aria-label="Faint hand-lettered signature of Helen Vorst"></div>
    <h1 class="agent-name">Helen Vorst</h1>
    <div class="brokerage-mark"><span class="dot"></span>Urban Parkview</div>
    <div class="phones">
      <div>404.555.0183<span class="tag">c</span></div>
      <div>404.555.0127<span class="tag">o</span></div>
      <div>404.555.0164<span class="tag">f</span></div>
    </div>
    <div class="office">
      <div>HO/LUXUrban Atlanta Parkview</div>
      <div class="address">2274 N. Halvers Brook Avenue</div>
      <div class="address">Halvers Park, GA 30390</div>
    </div>
  </section>
  <div class="accent-rule"></div>
  <div class="contact-band">
    <span>www.thecorelane.com</span><span>|</span>
    <span>Helen@thecorelane.com</span><span>|</span>
    <span>Helen@helenvorst.com</span>
  </div>

  <section class="card-back">
    <div class="signature-bright" role="img" aria-label="Hand-lettered signature of Helen Vorst in white"></div>
    <p class="tagline">Your Realtor</p>
    <p class="back-url">www.thecorelane.com</p>
  </section>
</body>
</html>
```